Website Design for Business Law Firm

We have a logo and now we would like a web site design for our new website. Our small firm provides creative and aggressive transactional (not litigation) legal services to advise healthcare, technology, internet-based and traditional companies and investors in such companies on healthcare, technology, financing, mergers/acquisitions, real estate and other transactions, legal compliance and general corporate and business matters.

We would like to see a website design that is professional and appropriate for executives, professionals, investors and government regulators to visit, that conveys professionalism and competence while being a little edgy and modern - no typical legal motifs such as gavels, books, or scales of justice. We advise businesses and investors and guide them through complicated issues quickly, capably and differently from other law firms. We are part of the business team and get things done.

The logo is attached, and we like gray as a color to complement it. The intention of the logo is to convey that in a storm or challenging time, people come to this firm, and people come to this firm when they need the power and disruption to change things or shake them up.

I have also enclosed a picture of our business card for consideration.

On the other hand, you can check out the current simple site at www.venhollow.example to see we have used a space motif in the past to evoke that we help create stars (the nebula featured there). This is not a necessary part of the new website and it may look better without it.

We appreciate your creativity and look forward to designs.

Industry/Entity Type

Business

Requirements
Must have
• We anticipate the following pages, and you may submit different ideas for the different pages:
• 1. Landing page
• 2. Services pages - healthcare, IT/Technology, general counsel services, financings, mergers/acquisitions, mediation/arbitration, procurement and productization
• 3. About Us including contact information
• Our name and contact information:
• Quellane Law Firm, P.C.
• 8716 SW 19th Ave.
• Portland, OR 97213
• phone: 971.555.0143
• fax: 971.555.0187
Nice to have
• Please consider designs that enhance the impressions we are looking for
Should not have
• Please no gavels, scales of justice, law books, or similar traditional legal imagery.

```html
<!DOCTYPE html>
<html lang="en">
<head>
<meta charset="utf-8">
<title>Quellane Law Firm, P.C.</title>
<link rel="stylesheet" href="https://fonts.googleapis.com/css2?family=Ubuntu:wght@400;500&display=swap">
<style>
  :root {
    --charcoal: #333333;
    --panel: #537079;
    --ink: #2f2f2f;
    --paper: #ffffff;
    --soft-text: #f1f1f1;
    --sky-top: #3b3530;
    --sky-glow: #e2962f;
    --sky-low: #2a1d12;
  }
  * { margin: 0; padding: 0; box-sizing: border-box; }
  html, body { width: 1200px; height: 934px; overflow: hidden; background: var(--charcoal); }
  body { font-family: "Ubuntu", sans-serif; color: var(--paper); position: relative; }

  .site-header { position: absolute; left: 0; top: 0; width: 1200px; height: 182px; background: var(--charcoal); }
  .brand-name {
    position: absolute; left: 22px; top: 60px;
    font-size: 60px; font-weight: 400; letter-spacing: 32px; color: var(--paper); line-height: 1;
  }
  .brand-mark { position: absolute; left: 22px; top: 36px; width: 14px; height: 14px; background: var(--paper); }
  .contact-line { position: absolute; top: 68px; right: 22px; display: flex; align-items: center; font-size: 18px; }
  .contact-line svg { margin-right: 12px; }
  .contact-line .email { margin-right: 22px; }
  .postal-line { position: absolute; right: 22px; top: 108px; font-size: 20px; }

  .hero { position: absolute; left: 0; top: 182px; width: 1200px; height: 626px; }
  .hero-photo {
    position: absolute; inset: 0;
    background: linear-gradient(180deg, var(--sky-top) 0%, #6d5433 22%, #b4782e 45%, var(--sky-glow) 62%, #c5822c 78%, var(--sky-low) 100%);
  }

  .services-panel { position: absolute; left: 598px; top: 28px; width: 516px; height: 574px; background: var(--panel); border-radius: 12px; }
  .services-banner { position: absolute; left: 567px; top: 51px; width: 580px; height: 97px; }
  .services-title {
    position: absolute; left: 612px; top: 57px; width: 460px;
    font-size: 28px; font-weight: 500; line-height: 26px; color: var(--ink);
  }
  .service-list { list-style: none; position: absolute; left: 641px; top: 123px; width: 460px; }
  .service-list li {
    position: relative; height: 28.1px; padding-left: 25px;
    font-size: 18px; line-height: 28px; color: var(--soft-text);
  }
  .service-list li::before {
    content: ""; position: absolute; left: 0; top: 8px; width: 12px; height: 12px; border-radius: 50%;
    background: radial-gradient(circle at 40% 35%, #f4f4f4 0%, #c8c8c8 55%, #8f8f8f 100%);
  }
  .service-list li.group-break { margin-top: 5px; }

  .site-footer { position: absolute; left: 0; top: 808px; width: 1200px; height: 126px; background: var(--charcoal); }
  .footer-address { position: absolute; left: 22px; top: 23px; font-size: 19px; }
  .footer-credit { position: absolute; left: 22px; top: 57px; font-size: 13px; }
  .footer-copy { position: absolute; left: 22px; top: 82px; font-size: 16px; }
  .footer-brand {
    position: absolute; left: 918px; top: 42px; font-size: 30px; letter-spacing: 12px; line-height: 1; color: var(--paper);
  }
</style>
</head>
<body>
  <header class="site-header">
    <span class="brand-mark"></span>
    <div class="brand-name">QUELLANE</div>
    <div class="contact-line">
      <svg width="26" height="26" viewBox="0 0 26 26" aria-hidden="true">
        <rect x="0" y="0" width="26" height="26" rx="5" fill="#e6e6e6"/>
        <rect x="5" y="8" width="16" height="11" fill="none" stroke="#9a9a9a" stroke-width="1.4"/>
        <path d="M5 8 L13 14 L21 8" fill="none" stroke="#9a9a9a" stroke-width="1.4"/>
      </svg>
      <span class="email">info@quellane.example</span>
      <svg width="36" height="22" viewBox="0 0 36 22" aria-hidden="true">
        <path d="M2 8 Q18 -2 34 8 L31 12 L25 10 L25 6 Q18 4 11 6 L11 10 L5 12 Z" fill="#c9cdd2"/>
        <path d="M8 12 L28 12 L32 21 L4 21 Z" fill="#aeb4ba"/>
      </svg>
      <span>971.555.0143</span>
    </div>
    <div class="postal-line">Quellane Law Firm, P.C., P.O. Box 6021, Portland, OR 97208</div>
  </header>

  <section class="hero">
    <div class="hero-photo" role="img" aria-label="Silhouette of a kneeling figure in reflection against an amber sunset sky"></div>

    <div class="services-panel"></div>
    <svg class="services-banner" viewBox="0 0 580 97" aria-hidden="true">
      <polygon points="0,0 518,0 580,32 518,65 0,65" fill="var(--paper)"/>
      <polygon points="0,65 31,65 31,97" fill="#1c1c1c"/>
    </svg>
    <h1 class="services-title">Pragmatic, Creative Services for Innovative Businesses</h1>

    <ul class="service-list">
      <li>Strategic Alliances</li>
      <li>Business REIationships</li>
      <li>Outsourcing</li>
      <li>Procurements-Buying or Selling</li>
      <li>Licensing and Technology Exploitation</li>
      <li>Venture Formation and Startup</li>
      <li>Venture Financing</li>
      <li>Creative Private Financing Arrangements</li>
      <li>Mergers and Acquisitions</li>
      <li>Real Estate</li>
      <li>Contracts</li>
      <li>Audits, Analyses and Legal Project Management</li>
      <li class="group-break">Local Counsel for Transactions and Due Diligence</li>
      <li>Vendor Management</li>
      <li>Dispute Resolution</li>
      <li>Service as a Mediator or Arbitrator</li>
    </ul>
  </section>

  <footer class="site-footer">
    <div class="footer-address">Quellane Law Firm, P.C., P.O. Box 6021, Portland, OR 97208</div>
    <div class="footer-credit">Image Credit : Orbital Archive, ODA, M.Varden (Deepfield Imaging Service Institute/ODA) and the Lumen Ridge Skyfield Gallery Project Team</div>
    <div class="footer-copy">Copyright © Quellane Law Firm. All rights reserved.</div>
    <div class="footer-brand">QUELLANE</div>
  </footer>
</body>
</html>
```